TRN marine wildlife conservation strategy

The Harbourline Stewardship Union (trn-stewards.org) needs an illustration to explain in a captivating and clear fashion the influences and interactions underlying our marine wildlife conservation planning and policymaking process. This will be included in our forthcoming strategy paper, and widely presented in conferences. Ultimately, this illustration will help governments take the right decisions to protect wildlife and natural resources.
Guidelines:
Size: The illustration shall fit in a A4 page, and also render nicely on a projector screen (1920x1080)
Colors: Avoid too colorful and 'playful' color code
Text: - Case shall be consistent throughout the graphic (unlike the draft design provided)
Graphic elements:
- In the top right of the graphic there is supposed to be a map of Myanmar. The map is attached. Feel free to adjust the map colors and style to match the illustration.
The only key areas we shall include in the map are:
- Myanmar borders
- EEZ (green),
- state/region borders (dotted lines),
- two marine corridors (blue and light red).
Everything else shall be left out (such as minimap, legend, scale, compass, SEZ).
- On the bottom right, it's important for the national benefits to be presented as a Venn diagram like in the original draft illustration (three intersecting circles)
Any questions? Please ask: mpaley@trn-stewards.org
Thank you!
Target Market(s)
Scientists, policy makers.
Industry/Entity Type
Environment

```html
<!DOCTYPE html>
<html lang="en">
<head>
<meta charset="utf-8">
<title>TRN Marine Spatial Planning Strategy</title>
<link href="https://fonts.googleapis.com/css2?family=Alfa+Slab+One&family=Lato:wght@300;400;700&display=swap" rel="stylesheet">
<style>
  :root {
    --panel-top: #f2f2f2;
    --panel-bottom: #9d9d9d;
    --sky-blue: #5cb8ee;
    --sky-blue-deep: #3fa3e0;
    --ink: #141414;
    --arrow-grey: #4b4b4b;
    --ring-light: #e2e2e2;
    --ring-shade: #cfcfcf;
    --engage-ring: #c8d2dc;
    --core-field: #d3dce6;
    --venn-fill: rgba(228, 228, 228, 0.92);
    --white-line: rgba(255, 255, 255, 0.85);
  }
  * { margin: 0; padding: 0; box-sizing: border-box; }
  html, body { width: 1200px; height: 932px; overflow: hidden; }
  body {
    position: relative;
    background: linear-gradient(180deg, var(--panel-top) 0%, #d0d0d0 45%, var(--panel-bottom) 100%);
    font-family: "Lato", sans-serif;
    color: var(--ink);
  }
  .diagram { position: absolute; inset: 0; width: 1200px; height: 932px; }
  .pressure-card {
    position: absolute;
    background: var(--sky-blue);
    border-radius: 6px 70px 6px 70px;
    box-shadow: 0 4px 10px rgba(0,0,0,0.18);
    display: flex;
    align-items: center;
    justify-content: center;
    text-align: center;
    font-family: "Alfa Slab One", serif;
    font-size: 14px;
    line-height: 1.6;
    padding: 0 14px;
  }
  .pressure-card::after {
    content: "";
    position: absolute;
    inset: 12px;
    border: 1px solid var(--white-line);
    border-radius: 4px 58px 4px 58px;
    pointer-events: none;
  }
  .card-political { left: 229px; top: 15px; width: 245px; height: 123px; white-space: nowrap; }
  .card-growth { left: 19px; top: 171px; width: 316px; height: 173px; }
  .card-ecosystems { left: 332px; top: 727px; width: 316px; height: 174px; }
  .card-sectors {
    left: 27px; top: 363px; width: 273px; height: 538px;
    align-items: flex-start;
    padding-top: 30px;
  }
  .map-area {
    position: absolute;
    left: 888px; top: 18px; width: 230px; height: 437px;
    border-radius: 40px 60px 20px 80px;
    background: linear-gradient(160deg, #ffffff 0%, #f2f4f6 50%, #c9cfd6 100%);
    box-shadow: inset 0 0 0 1px rgba(90,120,150,0.25);
  }
  .display-type { font-family: "Alfa Slab One", serif; fill: var(--ink); }
  .ring-type { font-size: 17px; letter-spacing: 0.5px; }
  .core-type { font-size: 14px; fill: var(--ink); }
  .engage-type { font-family: "Lato", sans-serif; font-weight: 300; font-size: 13px; letter-spacing: 1.6px; fill: #4a4a4a; }
  .sector-label { font-family: "Lato", sans-serif; font-size: 11px; fill: #2a2a2a; }
  .venn-label { font-family: "Lato", sans-serif; font-weight: 700; font-size: 11.5px; fill: #1e1e1e; }
  .cycle-type { font-family: "Lato", sans-serif; font-size: 12px; letter-spacing: 1px; fill: #ffffff; }
  .benefits-title { font-size: 27px; }
</style>
</head>
<body>

<div class="map-area" role="img" aria-label="Map of Myanmar showing national borders, exclusive economic zone, dotted state and region borders and two marine corridors"></div>

<div class="pressure-card card-political">POLITICAL TRANSITION</div>
<div class="pressure-card card-growth">INCREASING DEVELOPMENTAL PRESSURES FROM RAPID ECONOMIC GROWTH</div>
<div class="pressure-card card-sectors">WEAK COORDINATION<br>BETWEEN MARIN<br>SECTORS</div>
<div class="pressure-card card-ecosystems">DECLINING MARINE AND COASTAL ECOSYSTEMS AND RESOURCES</div>

<svg class="diagram" viewBox="0 0 1200 932" xmlns="http://www.w3.org/2000/svg">
  <defs>
    <marker id="flow-head" markerUnits="userSpaceOnUse" markerWidth="48" markerHeight="48" refX="10" refY="24" orient="auto">
      <path d="M0 2 L44 24 L0 46 Z" fill="var(--arrow-grey)"/>
    </marker>
    <marker id="core-head" markerUnits="userSpaceOnUse" markerWidth="34" markerHeight="46" refX="4" refY="23" orient="auto">
      <path d="M0 0 L30 23 L0 46 Z" fill="var(--sky-blue-deep)"/>
    </marker>
    <radialGradient id="hub-fill" cx="50%" cy="40%" r="60%">
      <stop offset="0%" stop-color="#f4f4f4"/>
      <stop offset="100%" stop-color="#d6d6d6"/>
    </radialGradient>
    <polygon id="sector-hex" points="0,-57 49.4,-28.5 49.4,28.5 0,57 -49.4,28.5 -49.4,-28.5"/>

    <path id="arc-consensus" d="M495 226 A232 232 0 0 1 839.5 386.7"/>
    <path id="arc-capacity" d="M524 241 A205 205 0 0 1 815 445"/>
    <path id="arc-institutional" d="M838 475 A232 232 0 0 1 532 645"/>
    <path id="arc-arrangements" d="M788.5 529.5 A205 205 0 0 1 593 631"/>
    <path id="arc-knowledge" d="M478 617 A232 232 0 0 1 513 217"/>
    <path id="arc-engagement" d="M611 262 A165 165 0 1 1 610.9 262"/>
    <path id="arc-vision" d="M531.3 380.9 A92 92 0 0 1 681.5 368"/>
    <path id="arc-coordination" d="M697.5 395.5 A92 92 0 0 1 611 519"/>
    <path id="arc-decision" d="M579.5 513.5 A92 92 0 0 1 524.5 395.5"/>
    <path id="arc-benefits" d="M865.8 738.5 A180 180 0 0 1 1041.7 487.3"/>
    <path id="arc-adaptive" d="M872 392 Q930 330 985 372"/>
    <path id="arc-management" d="M880 432 Q935 470 990 410"/>
  </defs>

  <!-- flow arrows into the planning cycle -->
  <path d="M470 62 C560 50 610 110 628 190" fill="none" stroke="var(--arrow-grey)" stroke-width="24" marker-end="url(#flow-head)"/>
  <path d="M345 228 C390 190 440 180 488 190" fill="none" stroke="var(--arrow-grey)" stroke-width="22" marker-end="url(#flow-head)"/>
  <path d="M310 612 C340 610 355 585 362 562" fill="none" stroke="var(--arrow-grey)" stroke-width="20" marker-end="url(#flow-head)"/>
  <path d="M385 715 C400 680 440 660 484 660" fill="none" stroke="var(--arrow-grey)" stroke-width="20" marker-end="url(#flow-head)"/>

  <!-- planning cycle -->
  <g class="planning-cycle">
    <circle cx="611" cy="427" r="262" fill="var(--ring-light)" stroke="#f4f4f4" stroke-width="3" style="filter: drop-shadow(0 4px 8px rgba(0,0,0,0.25));"/>
    <path d="M857.2 337.4 A262 262 0 0 1 521.4 673.2 L547.7 600.8 A185 185 0 0 0 784.8 363.7 Z" fill="var(--ring-shade)"/>
    <circle cx="611" cy="427" r="165" fill="none" stroke="var(--engage-ring)" stroke-width="40"/>
    <circle cx="611" cy="427" r="145" fill="var(--core-field)"/>

    <text class="display-type ring-type"><textPath href="#arc-consensus" startOffset="50%" text-anchor="middle">CONSENSUS BUILDING</textPath></text>
    <text class="display-type ring-type"><textPath href="#arc-capacity" startOffset="50%" text-anchor="middle">AND CAPACITY DEVELOPMENT</textPath></text>
    <text class="display-type ring-type"><textPath href="#arc-institutional" startOffset="50%" text-anchor="middle">INSTITUTIONAL DEVELOPMENT OF</textPath></text>
    <text class="display-type ring-type"><textPath href="#arc-arrangements" startOffset="50%" text-anchor="middle">ARRANGEMENTS</textPath></text>
    <text class="display-type ring-type"><textPath href="#arc-knowledge" startOffset="50%" text-anchor="middle">DATA KNOWLEDGE STENGTHENING</textPath></text>

    <text class="engage-type" dy="4"><textPath href="#arc-engagement" startOffset="0%">STAKEHOLDER ENGAGEMENT       STAKEHOLDER ENGAGEMENT       STAKEHOLDER ENGAGEMENT</textPath></text>

    <g class="core-arrows" fill="none" stroke="var(--sky-blue)" stroke-width="30">
      <path d="M524.4 377 A100 100 0 0 1 683 357" marker-end="url(#core-head)"/>
      <path d="M705 392.8 A100 100 0 0 1 626 526" marker-end="url(#core-head)"/>
      <path d="M576.8 521 A100 100 0 0 1 520 385" marker-end="url(#core-head)"/>
    </g>
    <circle cx="611" cy="427" r="100" fill="none" stroke="#ffffff" stroke-width="1.2" stroke-dasharray="5 4" opacity="0.8"/>
    <text class="display-type core-type" dy="-2"><textPath href="#arc-vision" startOffset="50%" text-anchor="middle">SHARED VISION</textPath></text>
    <text class="display-type core-type" dy="-2"><textPath href="#arc-coordination" startOffset="50%" text-anchor="middle">COORDINATION</textPath></text>
    <text class="display-type core-type" dy="-2"><textPath href="#arc-decision" startOffset="50%" text-anchor="middle">DECISION SUPPORT</textPath></text>

    <circle cx="611" cy="427" r="70" fill="url(#hub-fill)"/>
    <text class="display-type" font-size="17" text-anchor="middle">
      <tspan x="611" y="408">MARINE</tspan>
      <tspan x="611" y="432">SPATIAL</tspan>
      <tspan x="611" y="456">PLANNING</tspan>
    </text>
  </g>

  <!-- marine sectors -->
  <g class="sector-hexes" fill="#d2d2d2" stroke="#4d4d4d" stroke-width="1" stroke-dasharray="4 3">
    <use href="#sector-hex" x="109" y="528"/>
    <use href="#sector-hex" x="219" y="530"/>
    <use href="#sector-hex" x="161" y="625"/>
    <use href="#sector-hex" x="106" y="722"/>
    <use href="#sector-hex" x="215" y="722"/>
    <use href="#sector-hex" x="159" y="819"/>
  </g>
  <g class="sector-label" text-anchor="middle">
    <text><tspan x="109" y="526">Coastal</tspan><tspan x="109" y="540">Tourism</tspan></text>
    <text><tspan x="219" y="518">Marine and</tspan><tspan x="219" y="532">Coastal</tspan><tspan x="219" y="546">Conservation</tspan></text>
    <text><tspan x="161" y="613">Navy and</tspan><tspan x="161" y="627">Marine</tspan><tspan x="161" y="641">Police</tspan></text>
    <text><tspan x="106" y="720">Marine</tspan><tspan x="106" y="734">Fisheries</tspan></text>
    <text><tspan x="215" y="710">Offshore Gas</tspan><tspan x="215" y="724">Exploration and</tspan><tspan x="215" y="738">Production</tspan></text>
    <text><tspan x="159" y="817">Maritime</tspan><tspan x="159" y="831">Transport</tspan></text>
  </g>

  <!-- adaptive management loop -->
  <path d="M872 392 Q930 330 978 366" fill="none" stroke="var(--arrow-grey)" stroke-width="26" marker-end="url(#flow-head)"/>
  <path d="M990 410 Q935 470 886 436" fill="none" stroke="var(--arrow-grey)" stroke-width="26" marker-end="url(#flow-head)"/>
  <text class="cycle-type" dy="4"><textPath href="#arc-adaptive" startOffset="50%" text-anchor="middle">ADAPTIVE</textPath></text>
  <text class="cycle-type" dy="4"><textPath href="#arc-management" startOffset="50%" text-anchor="middle">MANAGEMENT</textPath></text>

  <!-- map to benefits -->
  <path d="M1098 330 C1140 380 1140 460 1118 516" fill="none" stroke="var(--arrow-grey)" stroke-width="26" marker-end="url(#flow-head)"/>

  <!-- national benefits -->
  <text class="display-type benefits-title"><textPath href="#arc-benefits" startOffset="50%" text-anchor="middle">NATIONAL BENEFITS</textPath></text>
  <g class="venn" style="filter: drop-shadow(0 3px 6px rgba(0,0,0,0.25));">
    <circle cx="1031" cy="596" r="84" fill="var(--venn-fill)"/>
    <circle cx="961" cy="703" r="84" fill="var(--venn-fill)"/>
    <circle cx="1102" cy="703" r="84" fill="var(--venn-fill)"/>
  </g>
  <g fill="none" stroke="#4a90c8" stroke-width="1" stroke-dasharray="4 3">
    <circle cx="1031" cy="596" r="74"/>
    <circle cx="961" cy="703" r="74"/>
    <circle cx="1102" cy="703" r="74"/>
  </g>
  <g class="venn-label" text-anchor="middle">
    <text><tspan x="1031" y="574">ECONOMIC</tspan><tspan x="1031" y="588">VALUE</tspan></text>
    <text><tspan x="954" y="718">SOCIAL</tspan><tspan x="954" y="732">DEVELOPMENT</tspan></text>
    <text><tspan x="1113" y="718">ENVIRONMENTAL</tspan><tspan x="1113" y="732">SUSTAINABILITY</tspan></text>
  </g>
</svg>

</body>
</html>
```